BrookfieldVentures Business Card Design

Design business cards with attached ideas. I am open to several different ideas that would be interesting and innovative. What I have provided is logo and colors. Font should be Helvetica although it could be bold or light as needed. The design can be vertical or horizontal. The design should be more interesting than a standard business card. Files must be ready to send to a printer and in Illustrator format. The text with the five icons should be exact. Send me some ideas and I will get back to you right away. I need to choose a design within 3-5 days.

Target Market(s)

Business audience

Industry/Entity Type

Business

Contact Information for Business Card

Files should be ready to send to printer in illustrator format

Font styles to use
Sans Serif

Colors
3276b5

Requirements
Must have
• Use attached logo and two colors - blue / gray
• Include 5 offering icons and text on back
Nice to have
• Interesting and innovative design. Vertical or horizontal are both fine.

```html
<!DOCTYPE html>
<html lang="en">
<head>
<meta charset="utf-8">
<title>BrookfieldVentures Offerings Card</title>
<link rel="stylesheet" href="https://fonts.googleapis.com/css2?family=Arimo:wght@700&family=Open+Sans:wght@400&display=swap">
<style>
  :root {
    --brand-blue: #3082ee;
    --ink-gray: #4a5560;
    --band-gray: #4a5058;
    --paper: #ffffff;
  }
  html, body {
    margin: 0;
    padding: 0;
    overflow: hidden;
    background: var(--paper);
  }
  .card {
    position: relative;
    width: 1200px;
    height: 667px;
    background: var(--paper);
    overflow: hidden;
  }
  .card-title {
    position: absolute;
    left: 221px;
    top: 56px;
    margin: 0;
    font-family: "Open Sans", sans-serif;
    font-weight: 400;
    font-size: 43px;
    line-height: 1;
    color: var(--ink-gray);
    letter-spacing: -0.4px;
  }
  .card-title .brand-name {
    color: var(--brand-blue);
  }
  .offerings {
    position: absolute;
    left: 221px;
    top: 123px;
    margin: 0;
    padding: 0;
    list-style: none;
  }
  .offering {
    position: relative;
    height: 48px;
    margin-bottom: 14px;
  }
  .offering:nth-child(5) { margin-top: 1px; }
  .offering-marker {
    position: absolute;
    left: 0;
    top: 0;
    width: 48px;
    height: 48px;
    border-radius: 50%;
    background: var(--brand-blue);
  }
  .offering-text {
    position: absolute;
    left: 75px;
    top: 0;
    height: 48px;
    display: flex;
    align-items: baseline;
    line-height: 48px;
    white-space: nowrap;
  }
  .offering-name {
    width: 204px;
    font-family: "Arimo", sans-serif;
    font-weight: 700;
    font-size: 31px;
    color: var(--ink-gray);
  }
  .offering-desc {
    font-family: "Open Sans", sans-serif;
    font-size: 29px;
    color: var(--ink-gray);
  }
  .offering-desc::before {
    content: ":";
    font-family: "Arimo", sans-serif;
    font-weight: 700;
    margin-right: 8px;
  }
  .divider {
    position: absolute;
    left: 0;
    top: 461px;
    width: 100%;
    height: 14px;
    background: var(--band-gray);
  }
  .contact {
    position: absolute;
    left: 0;
    top: 485px;
    width: 100%;
    height: 182px;
    box-sizing: border-box;
    padding-bottom: 12px;
    background: var(--brand-blue);
    display: flex;
    flex-direction: column;
    align-items: center;
    justify-content: center;
    font-family: "Open Sans", sans-serif;
    font-size: 33px;
    line-height: 45px;
    color: var(--paper);
  }
</style>
</head>
<body>
<main class="card">
  <h1 class="card-title"><span class="brand-name">BrookfieldVentures</span> Offerings</h1>

  <ul class="offerings">
    <li class="offering">
      <span class="offering-marker" aria-hidden="true"></span>
      <span class="offering-text">
        <span class="offering-name">Concepts</span>
        <span class="offering-desc">Thought leadership white papers</span>
      </span>
    </li>
    <li class="offering">
      <span class="offering-marker" aria-hidden="true"></span>
      <span class="offering-text">
        <span class="offering-name">Curriculum</span>
        <span class="offering-desc">Short courses on strategy</span>
      </span>
    </li>
    <li class="offering">
      <span class="offering-marker" aria-hidden="true"></span>
      <span class="offering-text">
        <span class="offering-name">Coaching</span>
        <span class="offering-desc">Building your strategic leadership</span>
      </span>
    </li>
    <li class="offering">
      <span class="offering-marker" aria-hidden="true"></span>
      <span class="offering-text">
        <span class="offering-name">Consulting</span>
        <span class="offering-desc">Developing your strategic future</span>
      </span>
    </li>
    <li class="offering">
      <span class="offering-marker" aria-hidden="true"></span>
      <span class="offering-text">
        <span class="offering-name">ScoreCard</span>
        <span class="offering-desc">Balanced ScoreCard and software</span>
      </span>
    </li>
  </ul>

  <div class="divider"></div>

  <footer class="contact">
    <span class="contact-phone">615-555-0142</span>
    <span class="contact-web">BrookfieldVentures.com</span>
    <span class="contact-email">Dana@BrookfieldVentures.com</span>
  </footer>
</main>
</body>
</html>
```